Manufacturing company needs new business card.

I need a unique Business Card that will truly stand out. Nothing too busy. Simple is good, right? Not looking for a standard design either. No cookie cutter layout. I am just looking for something interesting and a bit different. Does't have to completely off the wall crazy, just not your run of the mill business card. Clean and modern with a touch of industrial.

Target Market(s)

Air conditioning industry, Architects, builders.

Industry/Entity Type

Business

Contact Information for Business Card

Details to be included on card are:

Peter Vance
Managing Director

T: 1300 847 519
M: 0428 593 174
W: www.brenvaleworks.com.au
E: peter.vance@brenvaleworks.com.au
A: 58 Harwick Lane, Sydney NSW 2000

Font styles to use
Sans Serif

Colors
0355a3
848484
fbfbfb

Requirements
Must have
• Card design must be landscape.

```html
<!DOCTYPE html>
<html lang="en">
<head>
<meta charset="utf-8">
<title>Brenvale Works – Business Card</title>
<link rel="stylesheet" href="https://fonts.googleapis.com/css2?family=Open+Sans:wght@400;600&display=swap">
<style>
  :root {
    --brand-blue: #0355a3;
    --back-blue: #2152a4;
    --brand-grey: #848484;
    --text-grey: #5a5a5a;
    --paper: #fbfbfb;
    --stage: #e9e9e9;
    --white: #ffffff;
  }
  * { margin: 0; padding: 0; box-sizing: border-box; }
  html, body {
    width: 1200px; height: 1000px; overflow: hidden;
    background: var(--stage);
    font-family: "Open Sans", Arial, sans-serif;
  }
  .canvas { position: relative; width: 1200px; height: 1000px; }
  .card {
    position: absolute; left: 266px; width: 666px; height: 398px;
    box-shadow: 0 2px 6px rgba(0,0,0,0.18);
  }
  .card--front { top: 74px; background: var(--paper); }
  .card--back  { top: 534px; height: 396px; background: var(--back-blue); }

  .brand { position: absolute; display: flex; align-items: center; gap: 22px; }
  .brand__square { width: 52px; height: 52px; border-radius: 4px; }
  .brand__name { font-size: 30px; font-weight: 600; letter-spacing: -0.3px; white-space: nowrap; }
  .card--front .brand { left: 32px; top: 68px; }
  .card--front .brand__square { background: var(--brand-blue); }
  .card--front .brand__name { color: var(--brand-blue); }
  .card--back .brand { left: 136px; top: 169px; }
  .card--back .brand__square { background: var(--white); width: 58px; height: 58px; }
  .card--back .brand__name { color: var(--white); font-size: 32px; }

  .person { position: absolute; right: 32px; top: 182px; text-align: right; }
  .person__name { color: var(--brand-blue); font-size: 24px; font-weight: 600; line-height: 1.2; }
  .person__title { color: var(--text-grey); font-size: 16px; line-height: 1.3; }

  .contacts { position: absolute; left: 32px; top: 228px; list-style: none; }
  .contacts__item {
    display: flex; align-items: center; gap: 9px;
    height: 26px; color: var(--text-grey); font-size: 16px;
  }
  .contacts__icon { width: 15px; height: 15px; fill: var(--brand-blue); flex: none; }
  .address { position: absolute; left: 32px; top: 337px; color: var(--text-grey); font-size: 16px; }
</style>
</head>
<body>
<main class="canvas">

  <section class="card card--front" aria-label="Business card front">
    <div class="brand">
      <span class="brand__square"></span>
      <span class="brand__name">Brenvale Works</span>
    </div>

    <div class="person">
      <p class="person__name">Peter Vance</p>
      <p class="person__title">Managing Director</p>
    </div>

    <ul class="contacts">
      <li class="contacts__item">
        <svg class="contacts__icon" viewBox="0 0 16 16" aria-hidden="true"><path d="M4 1h8a1 1 0 0 1 1 1v12a1 1 0 0 1-1 1H4a1 1 0 0 1-1-1V2a1 1 0 0 1 1-1zm.6 1.4v9.6h6.8V2.4zM8 12.6a.8.8 0 1 0 0 1.6.8.8 0 0 0 0-1.6z"/></svg>
        1300 847 519
      </li>
      <li class="contacts__item">
        <svg class="contacts__icon" viewBox="0 0 16 16" aria-hidden="true"><path d="M1 6c0-2 3-3 7-3s7 1 7 3v1.2h-3.4V5.6c-1-.4-2.2-.5-3.6-.5s-2.6.1-3.6.5v1.6H1zm3.5 1.6h7L14 13H2z"/></svg>
        0428 593 174
      </li>
      <li class="contacts__item">
        <svg class="contacts__icon" viewBox="0 0 16 16" aria-hidden="true"><path d="M1 3.5h14v9H1zm1.4 1.2L8 9l5.6-4.3z"/></svg>
        peter.vance@brenvaleworks.com.au
      </li>
      <li class="contacts__item">
        <svg class="contacts__icon" viewBox="0 0 16 16" aria-hidden="true"><path d="M1 2h14v10H9.2v1.6H12V15H4v-1.4h2.8V12H1zm1.4 1.4v7.2h11.2V3.4z"/></svg>
        www.brenvaleworks.com.au
      </li>
    </ul>

    <p class="address">58 Harwick Lane, Sydney NSW 2000</p>
  </section>

  <section class="card card--back" aria-label="Business card back">
    <div class="brand">
      <span class="brand__square"></span>
      <span class="brand__name">Brenvale Works</span>
    </div>
  </section>

</main>
</body>
</html>
```